Wedding Day Custom Wine Label - Tasmanian (Tamar Valley) wine

I am looking for a custom design that will be put on a wine label to commemorate a very good friend's wedding day.

We will need to be able to take the design and print it on to sticker labels that we can put on to wine bottles.

The bride and groom have asked for a simplistic label design (see example image attached). We need two labels. One for "Pinot Noir" wine and the other for "Chardonnay" wine. We would like the label to say:

The Hartwell's
Pinot Noir
2023
Tamar Valley

and for for the other wine variety:

The Hartwell's
Chardonnay
2023
Tamar Valley

smaller text below to say:

13.5% ALC/VOL 750ML
MEGAN & LIAM - 31.10.2024

I am happy to consider other variations - the bride & groom would prefer something minimalistic. Elegant and classy.

Target Market(s)

the bride & groom

Requirements
Must have
• Wedding date (31.10.2024). Wine type (Pinot Noir or Chardonnay).
Should not have
• images not essential

```html
<!DOCTYPE html>
<html lang="en">
<head>
<meta charset="utf-8">
<title>The Hartwells – Pinot Noir 2023 Wine Label</title>
<link rel="stylesheet" href="https://fonts.googleapis.com/css2?family=Great+Vibes&family=Bebas+Neue&family=Libre+Baskerville:ital@0;1&family=Montserrat:wght@700&family=Roboto:wght@400&display=swap">
<style>
  :root {
    --backdrop: #3b3735;
    --label-rim: #2b2928;
    --paper: #f3f2ef;
    --frame-line: #3a3a3a;
    --ink: #1f1f1f;
    --wine-red: #8e1a22;
    --ornament-grey: #a9a9a9;
    --scene-light: #e6e5e1;
    --scene-dark: #8d8c88;
  }
  html, body {
    margin: 0;
    padding: 0;
    width: 1078px;
    height: 1200px;
    overflow: hidden;
    background: var(--backdrop);
  }
  .canvas {
    position: relative;
    width: 1078px;
    height: 1200px;
  }
  .wine-label {
    position: absolute;
    left: 279px;
    top: 30px;
    width: 520px;
    height: 1140px;
  }
  .label-shape {
    position: absolute;
    inset: 0;
  }
  .label-content {
    position: absolute;
    inset: 0;
    text-align: center;
    color: var(--ink);
    overflow: hidden;
  }
  .variety-arch {
    position: absolute;
    left: 0;
    top: 70px;
    width: 520px;
    height: 110px;
  }
  .variety-text {
    font-family: "Libre Baskerville", serif;
    font-size: 27px;
    letter-spacing: 1px;
    fill: var(--wine-red);
  }
  .family-name {
    position: absolute;
    left: 30px;
    right: 30px;
    top: 236px;
    margin: 0;
    font-family: "Great Vibes", cursive;
    font-weight: 400;
    color: var(--ink);
    line-height: 1;
  }
  .family-name .article {
    display: block;
    font-size: 46px;
    margin-left: 150px;
    margin-bottom: -22px;
  }
  .family-name .surname {
    display: block;
    font-size: 108px;
    letter-spacing: -1px;
    white-space: nowrap;
  }
  .vintage {
    position: absolute;
    left: 155px;
    width: 210px;
    top: 402px;
    padding: 6px 0 4px;
    border-top: 1px solid var(--frame-line);
    border-bottom: 1px solid var(--frame-line);
    font-family: "Libre Baskerville", serif;
    font-style: italic;
    font-size: 38px;
    letter-spacing: 9px;
    color: var(--wine-red);
    line-height: 1.1;
  }
  .vineyard-scene {
    position: absolute;
    left: 58px;
    top: 482px;
    width: 404px;
    height: 340px;
    background: linear-gradient(180deg, var(--paper) 0%, var(--scene-light) 28%, var(--scene-dark) 100%);
    border-radius: 4px;
  }
  .region {
    position: absolute;
    left: 0;
    right: 0;
    top: 858px;
    margin: 0;
    font-family: "Bebas Neue", sans-serif;
    font-weight: 400;
    font-size: 64px;
    letter-spacing: 2px;
    line-height: 1;
    color: var(--ink);
  }
  .specs {
    position: absolute;
    left: 155px;
    width: 210px;
    top: 946px;
    font-family: "Montserrat", sans-serif;
    font-weight: 700;
    font-size: 19px;
    color: var(--ink);
  }
  .specs .volume {
    padding-bottom: 6px;
    border-bottom: 1px solid var(--frame-line);
  }
  .specs .strength {
    padding: 7px 0 6px;
    border-bottom: 1px solid var(--frame-line);
  }
  .dedication {
    position: absolute;
    left: 0;
    right: 0;
    top: 1034px;
    font-family: "Roboto", sans-serif;
    font-size: 18px;
    color: #3a3a3a;
  }
</style>
</head>
<body>
<div class="canvas">
  <div class="wine-label">
    <svg class="label-shape" viewBox="0 0 520 1140" width="520" height="1140" aria-hidden="true">
      <path fill="var(--label-rim)" d="M44,0 H476 A44 44 0 0 0 520,44 V1096 A44 44 0 0 0 476,1140 H44 A44 44 0 0 0 0,1096 V44 A44 44 0 0 0 44,0 Z"/>
      <path fill="var(--paper)" d="M52,8 H468 A44 44 0 0 0 512,52 V1088 A44 44 0 0 0 468,1132 H52 A44 44 0 0 0 8,1088 V52 A44 44 0 0 0 52,8 Z"/>
      <path fill="none" stroke="var(--frame-line)" stroke-width="1.5" d="M62,24 H458 A38 38 0 0 0 496,62 V1078 A38 38 0 0 0 458,1116 H62 A38 38 0 0 0 24,1078 V62 A38 38 0 0 0 62,24 Z"/>
    </svg>

    <div class="label-content">
      <svg class="variety-arch" viewBox="0 0 520 110" width="520" height="110">
        <defs>
          <path id="variety-curve" d="M150,72 Q260,22 370,72"/>
        </defs>
        <path fill="none" stroke="var(--ornament-grey)" stroke-width="2" d="M150,40 Q260,0 370,40"/>
        <circle cx="150" cy="40" r="4" fill="none" stroke="var(--ornament-grey)" stroke-width="2"/>
        <circle cx="370" cy="40" r="4" fill="none" stroke="var(--ornament-grey)" stroke-width="2"/>
        <text class="variety-text" text-anchor="middle">
          <textPath href="#variety-curve" startOffset="50%">PINOT NOIR</textPath>
        </text>
        <path fill="none" stroke="var(--ornament-grey)" stroke-width="2" d="M160,92 Q260,58 360,92"/>
        <circle cx="160" cy="92" r="4" fill="none" stroke="var(--ornament-grey)" stroke-width="2"/>
        <circle cx="360" cy="92" r="4" fill="none" stroke="var(--ornament-grey)" stroke-width="2"/>
      </svg>

      <h1 class="family-name">
        <span class="article">The</span>
        <span class="surname">Hartwells</span>
      </h1>

      <div class="vintage">2023</div>

      <div class="vineyard-scene" role="img" aria-label="Engraved-style illustration of vineyard rows leading along a path towards rolling hills, farmhouses, cypress trees and birds in the sky"></div>

      <h2 class="region">TAMAR VALLEY</h2>

      <div class="specs">
        <div class="volume">750ML</div>
        <div class="strength">13.5% ALC/VOL</div>
      </div>

      <div class="dedication">Megan &amp; Liam - 31.10.2024</div>
    </div>
  </div>
</div>
</body>
</html>
```